Roaming outings business card

please see website
www.roamingoutings.comau

info needed on card
Keiran Voss
Ph
email
Adventure Riding GPS trails

please use my logo and colours off my site

Business

Keiran Voss
keiran@roamingoutings.com

```html
<!DOCTYPE html>
<html lang="en">
<head>
<meta charset="utf-8">
<title>Roaming outings business card</title>
<link rel="stylesheet" href="https://fonts.googleapis.com/css2?family=Lato:wght@400;700;900&display=swap">
<style>
  :root {
    --page: #e9e9e9;
    --card-white: #ffffff;
    --card-dark: #3a3a3a;
    --accent-red: #d9434c;
    --text-light: #f2f2f2;
    --text-dark: #1c1c1c;
  }
  * { margin: 0; padding: 0; box-sizing: border-box; }
  html, body {
    width: 1200px; height: 1200px; overflow: hidden;
    background: var(--page);
    font-family: "Lato", sans-serif;
  }
  .business-card {
    position: absolute; left: 100px; top: 310px;
    width: 1000px; height: 580px;
    background: var(--card-dark);
    box-shadow: 0 12px 30px rgba(0,0,0,0.25);
    overflow: hidden;
  }
  .edge-stripe {
    position: absolute; left: 0; top: 0; width: 36px; height: 100%;
    background: var(--accent-red);
  }
  .brand-panel {
    position: absolute; left: 36px; top: 0; width: 404px; height: 100%;
    background: var(--card-white);
    display: flex; align-items: center; justify-content: center; gap: 18px;
  }
  .brand-dot {
    width: 64px; height: 64px; border-radius: 50%;
    background: var(--accent-red); flex: none;
  }
  .brand-name {
    font-weight: 900; font-size: 34px; line-height: 1.05;
    color: var(--text-dark); text-transform: uppercase;
  }
  .divider-band {
    position: absolute; left: 440px; top: 0; width: 36px; height: 100%;
    background: var(--accent-red);
    box-shadow: -4px 0 8px rgba(0,0,0,0.15);
  }
  .band-icon {
    position: absolute; border-radius: 50%;
    background: var(--accent-red);
    display: flex; align-items: center; justify-content: center;
  }
  .band-icon.person { left: 430px; top: 84px; width: 56px; height: 56px; }
  .band-icon.small { left: 438px; width: 40px; height: 40px; }
  .band-icon svg { fill: #fff; }
  .holder-name {
    position: absolute; left: 510px; top: 88px;
    font-size: 40px; font-weight: 400; letter-spacing: 1px;
    color: var(--text-light); text-transform: uppercase;
  }
  .contact-list {
    position: absolute; left: 510px; top: 312px;
    color: var(--text-light); font-size: 22px; line-height: 1.25;
  }
  .contact-list .phone { margin-top: 22px; }
  .contact-list .tagline { margin-top: 30px; }
</style>
</head>
<body>
  <div class="business-card">
    <div class="edge-stripe"></div>
    <div class="brand-panel">
      <span class="brand-dot"></span>
      <span class="brand-name">Roaming<br>outings</span>
    </div>
    <div class="divider-band"></div>

    <div class="band-icon person">
      <svg width="30" height="30" viewBox="0 0 24 24" aria-hidden="true">
        <circle cx="12" cy="7" r="4.5"/><path d="M3 22c0-5 4-8 9-8s9 3 9 8z"/>
      </svg>
    </div>
    <div class="band-icon small" style="top:306px">
      <svg width="22" height="22" viewBox="0 0 24 24" aria-hidden="true">
        <path d="M2 6h20v12H2z" fill="none" stroke="#fff" stroke-width="2"/><path d="M2 6l10 7 10-7" fill="none" stroke="#fff" stroke-width="2"/>
      </svg>
    </div>
    <div class="band-icon small" style="top:368px">
      <svg width="22" height="22" viewBox="0 0 24 24" aria-hidden="true">
        <path d="M6.6 10.8a15 15 0 0 0 6.6 6.6l2.2-2.2a1 1 0 0 1 1-.25 11.4 11.4 0 0 0 3.6.6 1 1 0 0 1 1 1V20a1 1 0 0 1-1 1A17 17 0 0 1 3 4a1 1 0 0 1 1-1h3.5a1 1 0 0 1 1 1 11.4 11.4 0 0 0 .6 3.6 1 1 0 0 1-.25 1z"/>
      </svg>
    </div>
    <div class="band-icon small" style="top:430px">
      <svg width="22" height="22" viewBox="0 0 24 24" aria-hidden="true">
        <path d="M12 3l10 9h-3v9h-5v-6h-4v6H5v-9H2z"/>
      </svg>
    </div>

    <div class="holder-name">Keiran Voss</div>
    <div class="contact-list">
      <div class="email">keiran@roamingoutings.com</div>
      <div class="web">www.roamingoutings.comau</div>
      <div class="phone">555 018 2046</div>
      <div class="tagline">Adventure Riding GPS trails</div>
    </div>
  </div>
</body>
</html>
```